Ridgeway Sparks Business cards

We require somebody to design business cards for our new business.

Target Market(s)

Mining, haulage and civil.

Industry/Entity Type

Auto electrician in mining industry

Contact Information for Business Card

ABN, business email address, mobile number.

Colors
00AB8E
00BBA5
67D7C9
C6EFE9
E9F9F6

Requirements
Must have
• Services I offer: Breakdowns, Field Service, A/C Systems, Machine rewires, mine site vehicle fit outs

```html
<!DOCTYPE html>
<html lang="en">
<head>
<meta charset="utf-8">
<title>Ridgeway Sparks – Business Cards</title>
<link rel="stylesheet" href="https://fonts.googleapis.com/css2?family=Saira:wght@400;500;600;700&display=swap">
<style>
  :root {
    --backdrop: #e4e4e4;
    --card-top: #424242;
    --card-bottom: #2f2f2f;
    --teal: #5ccfc3;
    --teal-deep: #00bba5;
    --ink-light: #f2f2f2;
    --ink-muted: #bdbdbd;
    --divider: #6a6a6a;
    --emboss: #4c4c4c;
    --emboss-soft: #5e5e5e;
  }
  * { margin: 0; padding: 0; box-sizing: border-box; }
  html, body { width: 1200px; height: 1200px; overflow: hidden; }
  body {
    background: var(--backdrop);
    font-family: "Saira", sans-serif;
    position: relative;
  }
  .card {
    position: absolute;
    width: 687px;
    height: 392px;
    border-radius: 24px;
    background: linear-gradient(180deg, var(--card-top), var(--card-bottom));
    overflow: hidden;
  }
  .card--front { left: 267px; top: 159px; }
  .card--back  { left: 262px; top: 654px; }

  .brand-mark {
    position: absolute;
    left: 0; width: 344px;
    top: 0; height: 392px;
    display: flex; align-items: center; justify-content: center;
    gap: 10px;
    white-space: nowrap;
  }
  .brand-mark__dot {
    flex: none;
    width: 12px; height: 12px; border-radius: 50%;
    background: var(--teal);
  }
  .brand-mark__name {
    font-weight: 700;
    font-size: 27px;
    letter-spacing: 0.3px;
    color: var(--teal);
    text-transform: uppercase;
  }
  .divider {
    position: absolute;
    left: 344px; top: 82px;
    width: 2px; height: 228px;
    background: linear-gradient(180deg, transparent, var(--divider) 20%, var(--divider) 80%, transparent);
  }
  .contact {
    position: absolute;
    left: 369px; top: 84px;
    color: var(--ink-light);
    white-space: nowrap;
  }
  .contact__name {
    font-weight: 700;
    font-size: 27px;
    line-height: 1;
    color: var(--teal);
    text-transform: uppercase;
  }
  .contact__role { font-size: 15.5px; line-height: 1.2; margin-top: 3px; }
  .contact__address { font-size: 15.5px; line-height: 21px; margin-top: 16px; }
  .contact__list { list-style: none; margin-top: 9px; }
  .contact__item {
    display: flex; align-items: center;
    font-size: 15.5px; line-height: 20.5px;
  }
  .contact__icon {
    flex: none;
    width: 14px; height: 14px; margin-right: 10px;
    fill: var(--teal-deep); stroke: var(--teal-deep);
  }
  .contact__abn {
    font-size: 13px; line-height: 18px; margin-top: 8px;
    letter-spacing: 1px;
    color: var(--ink-muted);
  }

  .back-mark {
    position: absolute; inset: 0;
    display: flex; flex-direction: column;
    align-items: center; justify-content: center;
    gap: 18px;
    white-space: nowrap;
  }
  .back-mark__name {
    font-weight: 700;
    font-size: 58px;
    line-height: 1;
    color: var(--emboss);
    text-transform: uppercase;
  }
  .services {
    list-style: none;
    display: flex; gap: 0;
    font-size: 12.5px;
    letter-spacing: 1.6px;
    text-transform: uppercase;
    color: var(--emboss-soft);
  }
  .services__item + .services__item::before {
    content: "•";
    margin: 0 9px;
  }
</style>
</head>
<body>
  <section class="card card--front" aria-label="Business card front">
    <div class="brand-mark">
      <span class="brand-mark__dot"></span>
      <span class="brand-mark__name">Ridgeway Sparks</span>
    </div>
    <div class="divider"></div>
    <div class="contact">
      <h1 class="contact__name">Dean Harlow</h1>
      <p class="contact__role">President</p>
      <p class="contact__address">42 Quarry Ridge Road<br>Kalgoorlie, WA 6430</p>
      <ul class="contact__list">
        <li class="contact__item">
          <svg class="contact__icon" viewBox="0 0 14 14" aria-hidden="true"><path stroke="none" d="M3 1l2.2 2.6-1.2 1.6c.8 1.8 2.2 3.2 4 4l1.6-1.2L12.2 10.2 11 12.6C6 12 2 8 1.4 3z"/></svg>
          0412-558-207
        </li>
        <li class="contact__item">
          <svg class="contact__icon" viewBox="0 0 14 14" aria-hidden="true"><rect x="3.5" y="1" width="7" height="12" rx="1.2" fill="none" stroke-width="1.5"/></svg>
          0438-916-340
        </li>
        <li class="contact__item">
          <svg class="contact__icon" viewBox="0 0 14 14" aria-hidden="true"><rect x="1" y="3" width="12" height="8.5" stroke="none"/><path d="M1 3.2l6 4.3 6-4.3" fill="none" stroke="#3a3a3a" stroke-width="1.2"/></svg>
          hello@ridgewaysparks.au
        </li>
        <li class="contact__item">
          <svg class="contact__icon" viewBox="0 0 14 14" aria-hidden="true"><circle cx="7" cy="7" r="6" stroke="none"/><path d="M4 4.5c1.5 0 2 1 1.5 2S4 8 5 9.5M9 3c-.5 1.5 1 2 2 2.5M8.5 8.5c1 0 1.5 1 1 2.5" fill="none" stroke="#3a3a3a" stroke-width="1"/></svg>
          www.ridgewaysparks.au
        </li>
      </ul>
      <p class="contact__abn">ABN 51 824 753 556</p>
    </div>
  </section>

  <section class="card card--back" aria-label="Business card back">
    <div class="back-mark">
      <span class="back-mark__name">Ridgeway Sparks</span>
      <ul class="services" aria-label="Services">
        <li class="services__item">Breakdowns</li>
        <li class="services__item">Field Service</li>
        <li class="services__item">A/C Systems</li>
        <li class="services__item">Machine Rewires</li>
      </ul>
      <ul class="services" aria-label="More services">
        <li class="services__item">Mine Site Vehicle Fit Outs</li>
      </ul>
    </div>
  </section>
</body>
</html>
```